Motivational Poster Series for Students at Truck Driving School

We are looking for a series of 3 motivational posters (18"X 24") to be used in classrooms at a truck driving school. The audience for the posters will be the students that are currently in school and the purpose of the posters is to be motivational pieces that will be displayed on the walls.

We have provided the quotes below that are to be used on each poster. We have also provided some example images from PixQuarry to give an idea on the backgrounds that we'd like to see on each poster. The images do not have to be exact, these are just examples of what we think will look good for each quote. Since this is a series, they can all be somewhat similar in look/feel - just with different images and quotes.

So, the basic idea is a background image/design with a quote being the main point of emphasis. Other than that, we would like to include the logo provided at a small scale in one of the corners of the poster as a watermark for branding purposes.

Below are the quotes for each of the 3 posters:

Poster 1 - “It’s very difficult to follow our dreams, but it’s even more difficult to forget them.” - Devan Kollur

Poster 2 - “Success doesn’t just come and find you, you have to go out and get it.” - Unknown

Poster 3 - “If you are not willing to learn, no one can help you. If you are determined to learn, no one can stop you.”
- Unknown

NOTE: these posters should be designed as 18" X 24" in size with 2 of them being landscape and one being portrait orientation (as shown in images provided below)

Below are some sample images to give an idea on what could be used as background design for each quote. The logo that should be used as a watermark in a corner for some subtle branding has been provided as well.

Target Market(s)

The target market for this series are truck drivers between the ages of 25-55. Mostly males.

Industry/Entity Type

Landscape

Requirements
Must have
• Quote featured, high quality background design/image, logo watermark

```html
<!DOCTYPE html>
<html lang="en">
<head>
<meta charset="utf-8">
<title>Success Poster – Halvern Driver Academy</title>
<link rel="stylesheet" href="https://fonts.googleapis.com/css2?family=Open+Sans:ital,wght@0,400;0,600;0,700;1,700&display=swap">
<style>
  :root {
    --sky-top: #1b46a6;
    --sky-mid: #3d6fc4;
    --sky-low: #9fbfe2;
    --grass: #6fae3a;
    --road: #4a4d52;
    --road-dark: #34363a;
    --quote-white: rgba(255, 255, 255, 0.78);
    --credit-white: #ffffff;
    --brand-panel: rgba(225, 225, 225, 0.88);
    --brand-ink: #2b2b2b;
    --brand-accent: #b3262b;
  }
  html, body {
    margin: 0;
    padding: 0;
    width: 1200px;
    height: 900px;
    overflow: hidden;
    background: #ffffff;
  }
  .poster {
    position: relative;
    width: 1200px;
    height: 900px;
    overflow: hidden;
    font-family: "Open Sans", Arial, sans-serif;
  }
  .poster__scene,
  .poster__quote {
    position: absolute;
    inset: 0;
    width: 1200px;
    height: 900px;
  }
  .quote__text { fill: var(--quote-white); font-family: "Open Sans", Arial, sans-serif; }
  .quote__mark { fill: rgba(255, 255, 255, 0.55); font-family: "Open Sans", Arial, sans-serif; font-weight: 700; font-style: italic; }
  .quote__credit { fill: var(--credit-white); font-family: "Open Sans", Arial, sans-serif; font-weight: 400; }
  .brand {
    position: absolute;
    left: 14px;
    top: 818px;
    width: 258px;
    height: 40px;
    background: var(--brand-panel);
    display: flex;
    align-items: center;
    gap: 10px;
    padding-left: 10px;
    box-sizing: border-box;
  }
  .brand__square {
    width: 20px;
    height: 20px;
    background: var(--brand-accent);
    flex: none;
  }
  .brand__name {
    color: var(--brand-ink);
    font-family: "Open Sans", Arial, sans-serif;
    font-weight: 700;
    font-size: 17px;
    letter-spacing: 0.2px;
    white-space: nowrap;
  }
</style>
</head>
<body>
<main class="poster">
  <svg class="poster__scene" viewBox="0 0 1200 900" role="img" aria-label="Photograph of a blue curtain-side truck driving along a country road under a blue sky with green fields">
    <defs>
      <linearGradient id="scene-gradient" x1="0" y1="0" x2="0" y2="1">
        <stop offset="0" stop-color="var(--sky-top)"/>
        <stop offset="0.35" stop-color="var(--sky-mid)"/>
        <stop offset="0.6" stop-color="var(--sky-low)"/>
        <stop offset="0.64" stop-color="var(--grass)"/>
        <stop offset="0.78" stop-color="var(--grass)"/>
        <stop offset="0.82" stop-color="var(--road)"/>
        <stop offset="1" stop-color="var(--road-dark)"/>
      </linearGradient>
    </defs>
    <rect width="1200" height="900" fill="url(#scene-gradient)"/>
  </svg>

  <svg class="poster__quote" viewBox="0 0 1200 900" aria-labelledby="quote-title">
    <title id="quote-title">Success doesn’t just come and find you, you have to go out and get it. – Unknown</title>
    <text class="quote__mark" x="20" y="300" font-size="330">“</text>
    <text class="quote__mark" x="880" y="860" font-size="330">”</text>
    <text class="quote__text" x="12" y="292" font-size="262" font-weight="600" textLength="1176" lengthAdjust="spacingAndGlyphs">Success</text>
    <text class="quote__text" x="12" y="408" font-size="74" font-weight="600" textLength="1176" lengthAdjust="spacingAndGlyphs">doesn’t just come and find you,</text>
    <text class="quote__text" x="12" y="537" font-size="110" font-weight="700" textLength="1176" lengthAdjust="spacingAndGlyphs">you have to go out</text>
    <text class="quote__text" x="80" y="692" font-size="170" font-weight="700" font-style="italic" textLength="980" lengthAdjust="spacingAndGlyphs">and get it</text>
    <text class="quote__credit" x="1176" y="805" font-size="46" text-anchor="end">-Unknown</text>
  </svg>

  <div class="brand">
    <span class="brand__square"></span>
    <span class="brand__name">Halvern Driver Academy</span>
  </div>
</main>
</body>
</html>
```